Design for Certificate

Design a certificate for training, providing our company logo such as attachments. Company's name is "ØSTRA Velmark Advisory Ltd", please refer to our company profile: https://www.ostra-velmark.example/company_info

The style of the current certificate is also attached, and another certificate of another company can be referred to. Psd & jpg are required for the final draft (the layers of psd are not merged). Thanks!

```html
<!DOCTYPE html>
<html lang="en">
<head>
<meta charset="utf-8">
<title>Certificate of Completion – ØSTRA Velmark Advisory Ltd</title>
<link rel="stylesheet" href="https://fonts.googleapis.com/css2?family=Montserrat:wght@500;600&family=Cormorant+Garamond:wght@500&display=swap">
<style>
  :root {
    --backdrop: #eeeeee;
    --paper: #f6e0cb;
    --paper-light: #f5e3c2;
    --paper-band: #f2d7ad;
    --gold: #c59a2a;
    --gold-soft: #d2ad4f;
  }
  * { box-sizing: border-box; margin: 0; padding: 0; }
  html, body {
    width: 1200px; height: 800px; overflow: hidden;
    background: var(--backdrop);
  }
  .certificate {
    position: absolute; left: 40px; top: 20px;
    width: 1120px; height: 760px;
    background: var(--paper);
    color: var(--gold);
    text-align: center;
    overflow: hidden;
  }
  .certificate__frame { position: absolute; inset: 0; }
  .sans { font-family: "Montserrat", sans-serif; font-weight: 600; text-transform: uppercase; }
  .serif { font-family: "Cormorant Garamond", serif; font-weight: 500; text-transform: uppercase; letter-spacing: 0.32em; }
  .block { position: absolute; left: 0; right: 0; }

  .title { top: 78px; font-size: 84px; line-height: 1; letter-spacing: 0.01em; }
  .subtitle { top: 160px; font-size: 38px; line-height: 1; letter-spacing: 0.04em; }
  .awarded { top: 232px; font-size: 19px; }
  .recipient { top: 262px; font-size: 64px; line-height: 1; letter-spacing: 0.02em; }
  .completed { top: 376px; font-size: 19px; }
  .course { top: 406px; font-size: 38px; line-height: 1.1; letter-spacing: 0.03em; }
  .session { top: 512px; font-size: 19px; }
  .session .date {
    font-family: "Montserrat", sans-serif; font-weight: 500;
    letter-spacing: 0.02em; font-size: 21px;
    border-bottom: 1.5px solid var(--gold); padding: 0 6px 4px;
  }

  .cert-number {
    position: absolute; left: 150px; top: 640px; width: 300px;
    font-size: 16px; padding-top: 10px; border-top: 1.5px solid var(--gold);
  }
  .issuer {
    position: absolute; left: 460px; top: 575px; width: 200px;
    display: flex; flex-direction: column; align-items: center; gap: 12px;
  }
  .issuer__mark { width: 58px; height: 58px; border: 1.5px solid var(--gold); }
  .issuer__name { font-size: 17px; letter-spacing: 0.28em; }
  .signatory {
    position: absolute; left: 680px; top: 560px; width: 290px;
  }
  .signatory__signature {
    height: 64px; margin: 0 30px 6px;
    background: linear-gradient(90deg, rgba(197,154,42,0) 0%, rgba(197,154,42,0.28) 50%, rgba(197,154,42,0) 100%);
    border-radius: 30px;
  }
  .signatory__role {
    font-size: 16px; line-height: 1.4; padding-top: 8px;
    border-top: 1.5px solid var(--gold);
  }
</style>
</head>
<body>
<main class="certificate">
  <svg class="certificate__frame" width="1120" height="760" viewBox="0 0 1120 760" aria-hidden="true">
    <polygon points="0,0 300,0 0,420" fill="var(--paper-band)" opacity="0.55"/>
    <polygon points="0,0 170,0 0,240" fill="var(--paper-light)" opacity="0.7"/>
    <polygon points="1120,300 1120,760 760,760" fill="var(--paper-band)" opacity="0.55"/>
    <polygon points="1120,500 1120,760 940,760" fill="var(--paper-light)" opacity="0.7"/>
    <rect x="62" y="52" width="996" height="656" fill="none" stroke="var(--gold)" stroke-width="3.5"/>
    <rect x="76" y="66" width="968" height="628" fill="none" stroke="var(--gold)" stroke-width="1.2"/>
    <rect x="36" y="26" width="58" height="58" fill="none" stroke="var(--gold-soft)" stroke-width="1"/>
    <rect x="1026" y="26" width="58" height="58" fill="none" stroke="var(--gold-soft)" stroke-width="1"/>
    <rect x="36" y="676" width="58" height="58" fill="none" stroke="var(--gold-soft)" stroke-width="1"/>
    <rect x="1026" y="676" width="58" height="58" fill="none" stroke="var(--gold-soft)" stroke-width="1"/>
    <line x1="62" y1="40" x2="300" y2="40" stroke="var(--gold)" stroke-width="4"/>
    <line x1="820" y1="40" x2="1058" y2="40" stroke="var(--gold)" stroke-width="4"/>
    <line x1="62" y1="720" x2="300" y2="720" stroke="var(--gold)" stroke-width="4"/>
    <line x1="820" y1="720" x2="1058" y2="720" stroke="var(--gold)" stroke-width="4"/>
    <g fill="var(--gold)">
      <line x1="280" y1="322" x2="840" y2="322" stroke="var(--gold)" stroke-width="1.5"/>
      <rect x="276" y="318" width="8" height="8" transform="rotate(45 280 322)"/>
      <rect x="836" y="318" width="8" height="8" transform="rotate(45 840 322)"/>
    </g>
  </svg>

  <h1 class="block sans title">Certificate</h1>
  <p class="block sans subtitle">of Completion</p>
  <p class="block serif awarded">This certificate is awarded to</p>
  <p class="block sans recipient">John Doe</p>
  <p class="block serif completed">Has successfully completed</p>
  <p class="block sans course">Brand Reputation Management<br>Training Course</p>
  <p class="block serif session">Sixteen hours, held on <span class="date">November 10, 2019</span></p>

  <p class="serif cert-number">Certificate No.</p>
  <div class="issuer">
    <span class="issuer__mark"></span>
    <span class="serif issuer__name">ØSTRA Velmark</span>
  </div>
  <div class="signatory">
    <div class="signatory__signature" role="img" aria-label="Handwritten signature of the Chief Technology Officer"></div>
    <p class="serif signatory__role">Chief Technology<br>Officer</p>
  </div>
</main>
</body>
</html>
```